LRV Website

We need a completely new modern design for our website www.lrv.org.au.

The Tenure Holders Alliance of Australia Inc is a non-profit, volunteer-run association representing owners of strata-titled residential developments. We provide education, information and lobbying to improve the management of apartment complexes and the lives of those living in them. We’re all about “owners helping owners”. More information on our organisation can be seen at www.lrv.org.au.

Our new logo (from a recent MarkPanel contest) is attached.

Target Market(s)

Primary audience - Owners of residential apartments - both resident owners and investor owners
Secondary audiences – current and potential sponsors; organisations providing products & services to Owners Corporations & Body Corporates

Industry/Entity Type

Non-Profit

Number of Pages Required

3 pages

Requirements
Must have
• We need:
- A design for the home page
- A design for 2-column content pages
- Fonts and colours for
* standard text
* H1, H2, H3 and H4 heading tags
* Bulleted and numbered lists
- A complementary colour scheme for the Calendar page
- A complementary breadcrumb format
- A standard format to display the associated tags for any content page

The above are described in more detail in the attached document.

The design should:
- be modern, uncluttered and clean
- reflect a sense of community, coupled with authority, professionalism and knowledge
- be a fixed width of 1000px

At a minimum the files we need are:
- The source file (PSD with all component layers is preferred, but not mandatory)
- JPG preview files
- Any stand-alone images as a PNG with transparent backgrounds
- Details of all fonts and sizes used (if they can’t be easily identified in the source files)

Note: The site is built with the Drupal CMS, so all page elements must be able to be clearly isolated.
Should not have
• Any fonts that are not freely available

```html
<!DOCTYPE html>
<html lang="en">
<head>
<meta charset="utf-8">
<title>LRV Website – Page Designs</title>
<link href="https://fonts.googleapis.com/css2?family=Arimo:ital,wght@0,400;0,700;1,400&family=Open+Sans:ital,wght@0,400;0,600;1,400&display=swap" rel="stylesheet">
<style>
:root{
  --backdrop:#efefef;
  --paper:#ffffff;
  --navy:#1b4a96;
  --navy-dark:#163c7e;
  --link:#2357a6;
  --orange:#d9941c;
  --ink:#222222;
  --muted:#777777;
  --rule:#e6dccb;
  --panel:#ebebeb;
  --notes:#f7f7f7;
  --cal-grey:#cccccc;
  --cal-line:#d8d8d8;
  --cal-today:#c6d8e8;
}
*{margin:0;padding:0;box-sizing:border-box}
html,body{width:1200px;height:627px;overflow:hidden;background:var(--backdrop)}
body{font-family:"Arimo",Arial,sans-serif;color:var(--ink)}
.canvas{width:1200px;height:627px;overflow:hidden;position:relative}
.stage{position:absolute;left:0;top:0;width:2576px;height:1346px;transform:scale(0.46584);transform-origin:0 0}
.page{position:absolute;top:0;width:770px;height:1346px}
.page-shape{position:absolute;left:0;top:0;width:770px;height:1346px}
.page > *:not(.page-shape){position:absolute}

/* header */
.tagline{left:430px;top:117px;font-family:"Open Sans",sans-serif;font-style:italic;font-size:9.5px;line-height:15px;letter-spacing:.6px;color:#666}
.brand{left:18px;top:166px;display:flex;align-items:center;gap:8px}
.brand-mark{width:46px;height:46px;background:var(--orange)}
.brand-name{font-size:13.5px;line-height:12px;letter-spacing:1.2px;color:var(--navy);text-transform:uppercase}
.search{left:576px;top:203px;width:153px;height:19px;border-radius:10px;background:linear-gradient(#3f78c9,#1f54a6)}
.search-icon{left:736px;top:205px;width:16px;height:16px}
.nav{left:0;top:233px;width:770px;height:28px;background:linear-gradient(#2157ab,var(--navy-dark));display:flex;list-style:none}
.nav li{font-size:10.5px;color:#fff;line-height:28px;padding:0 18px;border-right:1px solid #3b68b3}
.nav li:first-child{padding-left:24px}
.nav li.active{color:var(--orange);background:#143a78}

/* content */
.crumbs{top:281px;left:17px;font-size:8px;color:var(--ink)}
.crumbs a{color:var(--link);text-decoration:none}
.crumbs .here{color:var(--orange)}
.page-title{left:16px;top:319px;font-family:"Open Sans",sans-serif;font-size:16px;color:var(--orange);font-weight:400}
a{color:var(--orange)}

.post{left:17px;width:488px;border-bottom:1px solid var(--rule);padding-bottom:20px}
.post h2{font-size:12px;color:var(--link);text-decoration:underline;letter-spacing:.3px;font-weight:700}
.post .meta{font-size:7px;color:var(--muted);margin:3px 0 10px}
.post p{font-size:8.6px;line-height:11px}
.post p a{margin-left:4px}

.notes{background:var(--notes);padding:22px 16px}
.notes h3{font-size:12px;font-weight:400;color:#777;margin-bottom:16px}
.notes h4{font-size:10px;font-weight:400;margin-bottom:4px}
.tags{font-size:8.4px;line-height:11px;color:var(--orange)}
.tags span{margin-right:9px;white-space:nowrap;display:inline-block}

.sidebar{left:525px;top:276px;width:231px;height:875px;background:var(--panel);padding:18px 24px}
.side-h{font-family:"Open Sans",sans-serif;font-size:12.5px;color:var(--navy);font-weight:400;letter-spacing:.4px}
.field-label{font-size:7.5px;font-weight:700;margin-top:9px}
.field-label i{color:#d33;font-style:normal}
.field{width:183px;height:17px;background:#fff;border:1px solid #c8c8c8;margin-top:3px}
.login-btn{margin:10px 0 0 107px;width:75px;height:22px;border-radius:3px;background:linear-gradient(#2a62b8,#163c7e);color:#fff;font-size:9px;text-align:center;line-height:22px}
.small-link{font-size:7.5px;text-align:right;margin-top:6px;width:183px}
.forum a{display:block;font-size:8px;line-height:10px;padding:4px 0;border-bottom:1px solid #d9d9d9;width:176px}
.events-list{list-style:none;font-size:8.5px;line-height:11px}
.events-list li{position:relative;padding-left:11px;margin-bottom:10px}
.events-list li::before{content:"";position:absolute;left:0;top:4px;width:4px;height:4px;border-radius:50%;background:#111}
.events-list a{display:block;font-size:8px}
.topic-list a{display:block;font-size:8.4px;line-height:21.5px}
.feature-box{width:183px;background:#f4f4f4;padding:13px 20px;font-size:9px;line-height:19px;color:#888;letter-spacing:.4px}
.social{display:flex;gap:5px}
.social span{width:16px;height:16px;border-radius:2px}

.footer{font-size:7.5px;color:#444;text-align:right;right:4px}
.footer a{text-decoration:none}

/* members area */
.topic-panel{left:0;top:367px;width:187px;height:138px;background:#f5f5f5;padding:16px 17px}
.article{left:208px;width:480px}
.article h2{font-size:12.5px;color:var(--navy);font-weight:700;margin-bottom:9px}
.article p{font-size:8.4px;line-height:10.8px}
.article p + p{margin-top:10px}

/* calendar */
.views{top:364px;left:18px;font-size:8.5px;display:flex;gap:9px}
.calendar{left:18px;top:383px;width:725px;border-collapse:collapse;table-layout:fixed;font-size:8.5px}
.calendar col.week-col{width:8px}
.calendar .cal-head td{background:var(--cal-grey);height:16px;padding:0 4px}
.calendar .cal-head .prev{text-align:left}
.calendar .cal-head .month{text-align:center;color:#333}
.calendar .cal-head .next{text-align:right}
.calendar .cal-head a{color:var(--link)}
.calendar th{background:#d7d7d7;font-weight:700;color:#333;height:15px;font-size:8.5px;border-right:1px solid #f2f2f2}
.calendar td.week{font-size:6px;vertical-align:top;color:var(--link);border-left:1px solid var(--cal-line);padding-top:2px}
.calendar td.day{height:51px;border:1px solid var(--cal-line);vertical-align:top;text-align:right;padding:1px}
.calendar td.day b{display:inline-block;min-width:14px;padding:1px 2px;background:#e3ecf4;color:var(--link);font-size:8px;text-align:center}
.calendar td.empty{background:var(--cal-grey)}
.calendar td.today{background:var(--cal-today)}
</style>
</head>
<body>
<div class="canvas">
<div class="stage">

<!-- ============ HOME PAGE ============ -->
<section class="page" style="left:60px">
  <svg class="page-shape" viewBox="0 0 770 1346" aria-hidden="true"><path d="M0,157 Q290,70 770,90 L770,1182 Q360,1168 0,1256 Z" fill="#fff"/></svg>
  <p class="tagline">... owners helping owners<br>... representing strata title residential developments<br>... lobbying and sharing information to improve apartment living</p>
  <div class="brand"><span class="brand-mark"></span><span class="brand-name">Tenure<br>Holders<br>Alliance</span></div>
  <div class="search"></div>
  <svg class="search-icon" viewBox="0 0 16 16" aria-hidden="true"><circle cx="6" cy="6" r="4.5" fill="none" stroke="#1b4a96" stroke-width="1.8"/><line x1="9.3" y1="9.3" x2="14.5" y2="14.5" stroke="#1b4a96" stroke-width="2.2"/></svg>
  <ul class="nav"><li class="active">Home</li><li>About</li><li>News</li><li>Events</li><li>Membership</li><li>Sponsorship</li><li>Links</li><li>Contact</li><li>Members Only</li></ul>

  <p class="crumbs"><a href="#">Home</a></p>
  <h1 class="page-title">News &amp; information</h1>

  <article class="post" style="top:358px"><h2>Bye-bye to bylaws</h2><p class="meta">Submitted by admin on 9 December 2009</p><p>What happens when complaints get trampled underfoot. When is a bylaw not a bylaw? When the Residential, Lease and Strata Tribunal decides it doesn't really matter, that's when<a href="#">more</a></p></article>
  <article class="post" style="top:457px"><h2>Bye-bye to bylaws</h2><p class="meta">Submitted by admin on 9 December 2009</p><p>What happens when complaints get trampled underfoot. When is a bylaw not a bylaw? When the Residential, Lease and Strata Tribunal decides it doesn't really matter, that's when<a href="#">more</a></p></article>
  <article class="post" style="top:562px"><h2>Bye-bye to bylaws</h2><p class="meta">Submitted by admin on 9 December 2009</p><p>What happens when complaints get trampled underfoot. When is a bylaw not a bylaw? When the Residential, Lease and Strata Tribunal decides it doesn't really matter, that's when<a href="#">more</a></p></article>
  <article class="post" style="top:665px"><h2>Bye-bye to bylaws</h2><p class="meta">Submitted by admin on 9 December 2009</p><p>What happens when complaints get trampled underfoot. When is a bylaw not a bylaw? When the Residential, Lease and Strata Tribunal decides it doesn't really matter, that's when<a href="#">more</a></p></article>
  <article class="post" style="top:766px"><h2>Bye-bye to bylaws</h2><p class="meta">Submitted by admin on 9 December 2009</p><p>What happens when complaints get trampled underfoot. When is a bylaw not a bylaw? When the Residential, Lease and Strata Tribunal decides it doesn't really matter, that's when<a href="#">more</a></p></article>
  <article class="post" style="top:865px"><h2>Bye-bye to bylaws</h2><p class="meta">Submitted by admin on 9 December 2009</p><p>What happens when complaints get trampled underfoot. When is a bylaw not a bylaw? When the Residential, Lease and Strata Tribunal decides it doesn't really matter, that's when<a href="#">more</a></p></article>

  <div class="notes" style="left:18px;top:965px;width:487px;height:102px">
    <h3>Speaker Notes</h3><h4>TAGS</h4>
    <p class="tags"><span>building management rights</span><span>building manager</span><span>city of harbourvale</span><span>defects</span><span>digitalTV</span><span>finance</span><span>fire safety</span><span>insurance</span><span>legislation</span><span>ombudsman</span><span>recod keeping</span><span>security</span><span>strata managers</span></p>
  </div>

  <aside class="sidebar">
    <h3 class="side-h">Member Login</h3>
    <p class="field-label">Username or e-mail: <i>*</i></p><div class="field"></div>
    <p class="field-label">Password: <i>*</i></p><div class="field"></div>
    <div class="login-btn">Log in</div>
    <p class="small-link"><a href="#">Request new password</a></p>

    <h3 class="side-h" style="margin-top:20px">Recent forum posts</h3>
    <div class="forum" style="margin-top:8px">
      <a href="#">Discussion for Bye-bye to bylaws -<br>on 21 Apr 2010</a>
      <a href="#">Discussion for Bye-bye to bylaws -<br>on 21 Apr 2010</a>
      <a href="#" style="border:0">Discussion for Bye-bye to bylaws -<br>on 21 Apr 2010</a>
    </div>

    <h3 class="side-h" style="margin-top:24px">Upcoming Events</h3>
    <ul class="events-list" style="margin-top:12px">
      <li>20 Feb 2010 - 10:00am - 12:00pm<a href="#">LRV General Meeting</a></li>
      <li>24 Feb 2010 - 6:15pm - 7:45pm<a href="#">QBRT Consumer Awareness Seminar</a></li>
      <li>21 Apr 2010 - 6:15pm - 7:45pm<a href="#">QBRT Consumer Awareness Seminar</a></li>
      <li>15 May 2010 - 10:00am - 12:00pm<a href="#">LRV General Meeting</a></li>
    </ul>

    <h3 class="side-h" style="margin-top:28px">Topic List</h3>
    <div class="topic-list" style="margin-top:6px;padding-left:2px">
      <a href="#">LRV General Meeting</a><a href="#">QBRT Consumer Awareness Seminar</a><a href="#">QBRT Consumer Awareness Seminar</a><a href="#">LRV General Meeting</a>
    </div>

    <h3 class="side-h" style="margin-top:20px">Feature announcements</h3>
    <div class="feature-box" style="margin-top:17px">Feature announcements that may be posted occasionally</div>

    <div class="social" style="margin:128px 0 0 86px">
      <span style="background:#3b5fa8"></span><span style="background:#8fd0ea"></span><span style="background:#f08a24"></span><span style="background:#3a8fd6"></span><span style="background:#2b7bc4"></span>
    </div>
  </aside>

  <p class="footer" style="top:1204px">©Tenure Holders Alliance Inc 2010 | <a href="#">Disclaimer</a> | <a href="#">Contact Us</a></p>
</section>

<!-- ============ MEMBERS AREA ============ -->
<section class="page" style="left:900px">
  <svg class="page-shape" viewBox="0 0 770 1346" aria-hidden="true"><path d="M0,157 Q290,70 770,90 L770,917 Q350,905 0,987 Z" fill="#fff"/></svg>
  <p class="tagline">... owners helping owners<br>... representing strata title residential developments<br>... lobbying and sharing information to improve apartment living</p>
  <div class="brand"><span class="brand-mark"></span><span class="brand-name">Tenure<br>Holders<br>Alliance</span></div>
  <div class="search"></div>
  <svg class="search-icon" viewBox="0 0 16 16" aria-hidden="true"><circle cx="6" cy="6" r="4.5" fill="none" stroke="#1b4a96" stroke-width="1.8"/><line x1="9.3" y1="9.3" x2="14.5" y2="14.5" stroke="#1b4a96" stroke-width="2.2"/></svg>
  <ul class="nav"><li>Home</li><li>About</li><li>News</li><li>Events</li><li class="active">Membership</li><li>Sponsorship</li><li>Links</li><li>Contact</li><li>Members Only</li></ul>

  <p class="crumbs">Home &gt; <span class="here">Members Area</span></p>
  <h1 class="page-title" style="top:321px">Members Area</h1>

  <aside class="topic-panel">
    <h3 class="side-h">Topic List</h3>
    <div class="topic-list" style="margin-top:4px">
      <a href="#">LRV General Meeting</a><a href="#">QBRT Consumer Awareness Seminar</a><a href="#">QBRT Consumer Awareness Seminar</a><a href="#">LRV General Meeting</a>
    </div>
  </aside>

  <article class="article" style="top:364px"><h2>Building Management Rights - Buyers Beware</h2>
    <p>Lorem ipsum dolor sit amet, consectetur adipiscing elit. Maecenas eget risus neque. Nullam sollicitudin lobortis turpis quis ultricies sapien adipiscing id. Lorem ipsum dolor sit amet, consectetur adipiscing elit. Morbi dapibus lacinia urna, sed pulvinar metus fringilla in. Nulla sit amet enim justo, vel accumsan dolor. Fusce et nulla ut est sagittis varius id n c enim. Vivamus vestibulum porttitor dolor vel posuere. Praesent tempus, turpis vitae bibendum mollis, dui quis tristiqu e ligula, vitae molestie lacus leo ut arcu. Sed quis eros dui. Nullam pulvinar tortor ac dui laoreet i</p>
    <p>s llicitudin dolor lectus eget erat. Aliquam dapibus, dolor vitae sagittis sollicitudin, ipsum tortor pretium nisi, vit ae pellentesque elit risus et turpis. Fusce a tortor ac magna volutpat mattis.</p>
  </article>
  <article class="article" style="top:504px"><h2>Building Owners &amp; Occupiers - How up to date must they be (A&amp;1851)?</h2>
    <p>quis ultricies sapien adipiscing id. Lorem ipsum dolor sit amet, consectetur adipiscing elit. Morbi dapibus lacinia urna, sed pulvinar metus fringilla in. Nulla sit amet enim justo, vel accumsan dolor. Fusce et nulla ut est sagittis varius id n c enim. Vivamus vestibulum porttitor dolor vel posuere. Praesent tempus, turpis vitae bibendum mollis, dui quis tristiqu e ligula, vitae molestie lacus leo ut arcu. Sed quis eros dui. Nullam pulvinar tortor ac dui laoreet i</p>
  </article>
  <article class="article" style="top:601px"><h2>Defects</h2>
    <p>quis ultricies sapien adipiscing id. Lorem ipsum dolor sit amet, consectetur adipiscing elit. Morbi dapibus lacinia urna, sed pulvinar metus fringilla in. Nulla sit amet enim justo, vel accumsan dolor. Fusce et nulla ut est sagittis varius id n c enim. Vivamus vestibulum porttitor dolor vel posuere. Praesent tempus, turpis vitae bibendum mollis, dui quis tristiqu e ligula, vitae molestie lacus leo ut arcu. Sed quis eros dui. Nullam pulvinar tortor ac dui laoreet i</p>
  </article>
  <article class="article" style="top:698px"><h2>Demystifying High-Rise Fire Safety</h2>
    <p>quis ultricies sapien adipiscing id. Lorem ipsum dolor sit amet, consectetur adipiscing elit. Morbi dapibus lacinia urna, sed pulvinar metus fringilla in. Nulla sit amet enim justo, vel accumsan dolor. Fusce et nulla ut est sagittis varius id n c enim. Vivamus vestibulum porttitor dolor vel posuere. Praesent tempus, turpis vitae bibendum mollis, dui quis tristiqu e ligula, vitae molestie lacus leo ut arcu. Sed quis eros dui. Nullam pulvinar tortor ac dui laoreet i</p>
  </article>

  <div class="notes" style="left:17px;top:778px;width:728px;height:102px">
    <h3>Speaker Notes</h3><h4>TAGS</h4>
    <p class="tags"><span>building management rights</span><span>building manager</span><span>city of harbourvale</span><span>defects</span><span>digitalTV</span><span>finance</span><span>fire safety</span><span>insurance</span><span>legislation</span><span>ombudsman</span><span>recod keeping</span><br><span>security</span><span>strata managers</span></p>
  </div>

  <p class="footer" style="top:935px">©Tenure Holders Alliance Inc 2010 | <a href="#">Disclaimer</a> | <a href="#">Contact Us</a></p>
</section>

<!-- ============ EVENTS ============ -->
<section class="page" style="left:1739px">
  <svg class="page-shape" viewBox="0 0 770 1346" aria-hidden="true"><path d="M0,157 Q290,70 770,90 L770,887 Q350,875 0,957 Z" fill="#fff"/></svg>
  <p class="tagline">... owners helping owners<br>... representing strata title residential developments<br>... lobbying and sharing information to improve apartment living</p>
  <div class="brand"><span class="brand-mark"></span><span class="brand-name">Tenure<br>Holders<br>Alliance</span></div>
  <div class="search"></div>
  <svg class="search-icon" viewBox="0 0 16 16" aria-hidden="true"><circle cx="6" cy="6" r="4.5" fill="none" stroke="#1b4a96" stroke-width="1.8"/><line x1="9.3" y1="9.3" x2="14.5" y2="14.5" stroke="#1b4a96" stroke-width="2.2"/></svg>
  <ul class="nav"><li>Home</li><li>About</li><li>News</li><li class="active">Events</li><li>Membership</li><li>Sponsorship</li><li>Links</li><li>Contact</li><li>Members Only</li></ul>

  <p class="crumbs">Home &gt; <span class="here">Events</span></p>
  <h1 class="page-title" style="top:321px">Events</h1>

  <nav class="views"><a href="#">Year</a><a href="#">Month</a><a href="#">Week</a><a href="#">Day</a></nav>

  <table class="calendar">
    <colgroup><col class="week-col"><col><col><col><col><col><col><col></colgroup>
    <tr class="cal-head"><td colspan="2" class="prev"><a href="#">« Prev</a></td><td colspan="4" class="month">January 2010</td><td colspan="2" class="next"><a href="#">Next »</a></td></tr>
    <tr><th></th><th>Sunday</th><th>Monday</th><th>Tuesday</th><th>Wednesday</th><th>Thursday</th><th>Friday</th><th>Saturday</th></tr>
    <tr><td class="week">1</td><td class="day empty" colspan="5"></td><td class="day"><b>1</b></td><td class="day"><b>2</b></td></tr>
    <tr><td class="week">2</td><td class="day"><b>3</b></td><td class="day"><b>4</b></td><td class="day"><b>5</b></td><td class="day"><b>6</b></td><td class="day"><b>7</b></td><td class="day"><b>8</b></td><td class="day"><b>9</b></td></tr>
    <tr><td class="week">3</td><td class="day"><b>10</b></td><td class="day"><b>11</b></td><td class="day today"><b>12</b></td><td class="day"><b>13</b></td><td class="day"><b>14</b></td><td class="day"><b>15</b></td><td class="day"><b>16</b></td></tr>
    <tr><td class="week">4</td><td class="day"><b>17</b></td><td class="day"><b>18</b></td><td class="day"><b>19</b></td><td class="day"><b>20</b></td><td class="day"><b>21</b></td><td class="day"><b>22</b></td><td class="day"><b>23</b></td></tr>
    <tr><td class="week">5</td><td class="day"><b>24</b></td><td class="day"><b>25</b></td><td class="day"><b>26</b></td><td class="day"><b>27</b></td><td class="day"><b>28</b></td><td class="day"><b>29</b></td><td class="day"><b>30</b></td></tr>
    <tr><td class="week">6</td><td class="day"><b>31</b></td><td class="day empty" colspan="6"></td></tr>
  </table>

  <div class="notes" style="left:18px;top:755px;width:728px;height:100px">
    <h3>Speaker Notes</h3><h4>TAGS</h4>
    <p class="tags"><span>building management rights</span><span>building manager</span><span>city of harbourvale</span><span>defects</span><span>digitalTV</span><span>finance</span><span>fire safety</span><span>insurance</span><span>legislation</span><span>ombudsman</span><span>recod keeping</span><br><span>security</span><span>strata managers</span></p>
  </div>

  <p class="footer" style="top:907px">©Tenure Holders Alliance Inc 2010 | <a href="#">Disclaimer</a> | <a href="#">Contact Us</a></p>
</section>

</div>
</div>
</body>
</html>
```